Vellart

I already have a website created through Makrive.com - https://vellart.co.nz.

Its an accounting services business, can get ideas from wexo.co.nz, fyn.co.nz, hul.co.nz

I would like to have this recreated using coding. I need the following features and functionalities incorporated:

- Live Chat feature
- Moving Carousel feature for Reviews
- Advanced SEO support (Google Analytics)

Industry/Entity Type

accounting

Coding

Coded - Design and coding required

Number of Pages Required

5+ page

```html
<!DOCTYPE html>
<html lang="en">
<head>
<meta charset="utf-8">
<title>Vellart – Accounting Services</title>
<link href="https://fonts.googleapis.com/css2?family=Barlow+Condensed:wght@600;700&family=Roboto:wght@400;500&display=swap" rel="stylesheet">
<style>
:root{
  --green-dark:#2f5a4e;
  --green:#3f7d6c;
  --green-mid:#5c9d8b;
  --teal-light:#a6d8cc;
  --teal-pale:#d8efe9;
  --ink:#2b2b2b;
  --text:#555;
  --slate:#2e3c39;
  --white:#fff;
  --peach:#f6d9c9;
}
*{box-sizing:border-box;margin:0;padding:0}
html,body{width:1200px;height:4197px;overflow:hidden}
body{position:relative;background:var(--white);font-family:"Roboto",sans-serif;color:var(--text)}
.abs{position:absolute}
.heading{font-family:"Barlow Condensed",sans-serif;font-weight:700;color:var(--ink);text-transform:uppercase;letter-spacing:.5px}
.btn{position:absolute;display:flex;align-items:center;justify-content:center;gap:12px;border-radius:6px 20px 6px 6px;font:500 15px "Roboto",sans-serif;color:var(--white);background:var(--green-dark)}
.btn--light{background:var(--teal-light);color:var(--green-dark)}
.btn svg{width:15px;height:15px}
.arrow-dot{display:inline-block}

/* header & hero */
.hero{position:absolute;left:0;top:0;width:1200px;height:660px;overflow:hidden}
.hero__sky{position:absolute;inset:0;background:linear-gradient(180deg,#f3d3c6 0%,#f4dbc8 35%,#cfd9dc 70%,#a9c2cc 100%)}
.hero__city{position:absolute;left:0;top:330px;width:1200px;height:230px;background:linear-gradient(180deg,#9fb7c6 0%,#7e9aa9 60%,#b7c8cf 100%)}
.hero__portrait{position:absolute;left:244px;top:57px;width:326px;height:470px;border-radius:160px 160px 0 0;background:linear-gradient(180deg,#e9dccd 0%,#c7b3a1 45%,#6d5c4f 100%)}
.brand{position:absolute;display:flex;align-items:center;gap:10px;font-family:"Roboto",sans-serif;font-weight:500;letter-spacing:4px;color:var(--green-dark);text-transform:uppercase}
.brand__dot{width:14px;height:14px;border-radius:50%;background:var(--green-dark)}
.nav{position:absolute;top:32px;left:430px;display:flex;gap:0;font:500 15px "Roboto",sans-serif;color:var(--ink)}
.nav a{position:absolute;white-space:nowrap;color:var(--ink);text-decoration:none}
.hero__bubble{position:absolute;left:573px;top:98px;width:480px;height:440px;border-radius:230px 200px 60px 90px;background:linear-gradient(160deg,#3f8a74 0%,#2f6b5a 60%,#4f9a85 100%)}
.hero__eyebrow{position:absolute;left:573px;top:160px;width:480px;text-align:center;font:500 18px "Roboto",sans-serif;color:var(--white);letter-spacing:.3px}
.hero__title{position:absolute;left:573px;top:188px;width:480px;text-align:center;font-family:"Barlow Condensed",sans-serif;font-weight:700;font-size:66px;line-height:66px;color:var(--white)}
.hero__lead{position:absolute;left:615px;top:326px;width:396px;text-align:center;font:400 17px/28px "Roboto",sans-serif;color:#eaf5f1}

/* about */
.about__title{position:absolute;left:110px;top:712px;font-size:42px}
.about__photo{position:absolute;left:110px;top:785px;width:341px;height:347px;border-radius:30px 0 0 30px;background:linear-gradient(135deg,#55575a 0%,#7b7c7f 40%,#4a4b4f 70%,#a98a6a 100%)}
.about__copy{position:absolute;left:508px;top:712px;width:581px;font:400 15px/30px "Roboto",sans-serif;text-align:justify}
.about__copy p+p{margin-top:16px}
.badge{position:absolute;display:flex;align-items:center;justify-content:center;gap:14px;height:40px;background:var(--white);border-radius:10px;box-shadow:0 6px 18px rgba(0,0,0,.12);font:700 16px "Barlow Condensed",sans-serif;color:var(--ink);text-transform:uppercase}
.badge svg{width:18px;height:18px}

/* features */
.features{position:absolute;left:0;top:1224px;width:1200px;height:125px;background:var(--white);box-shadow:0 -4px 20px rgba(0,0,0,.05)}
.feature{position:absolute;top:0;height:125px;text-align:left;font:400 16px "Roboto",sans-serif;color:#666}
.feature svg{position:absolute;top:22px;width:42px;height:42px}
.feature span{position:absolute;top:83px;white-space:nowrap}
.feature__rule{position:absolute;top:24px;width:2px;height:78px;background:#8a8a8a}

/* services */
.services{position:absolute;left:0;top:1349px;width:1200px;height:650px;background:linear-gradient(100deg,#c5e5dc 0%,#8fc6b7 45%,#3f7f6d 100%);overflow:hidden}
.services__title{position:absolute;left:110px;top:52px;font-size:40px;color:var(--white)}
.round-btn{position:absolute;width:34px;height:34px;border-radius:50%;background:var(--white);display:flex;align-items:center;justify-content:center;box-shadow:0 2px 6px rgba(0,0,0,.15)}
.round-btn svg{width:14px;height:14px}
.svc{position:absolute;width:233px}
.svc__photo{position:absolute;left:0;top:0;width:233px;height:245px;border-radius:20px}
.svc__box{position:absolute;left:17px;top:192px;width:200px;height:128px;background:var(--white);border-radius:10px;text-align:center;padding:20px 10px 0;box-shadow:0 4px 14px rgba(0,0,0,.1)}
.svc__box h3{font:700 17px "Barlow Condensed",sans-serif;color:var(--ink);text-transform:uppercase}
.svc__box p{margin-top:6px;font:400 12px/20px "Roboto",sans-serif;color:#555}
.svc__go{position:absolute;left:105px;top:308px;width:24px;height:24px;border-radius:50%;background:var(--green-dark);display:flex;align-items:center;justify-content:center}
.svc__go svg{width:11px;height:11px}

/* empower */
.empower__title{position:absolute;left:110px;top:2080px;font-size:42px;line-height:48px}
.empower__sub{position:absolute;left:110px;top:2182px;font-size:21px;color:var(--green-dark)}
.empower__copy{position:absolute;left:110px;top:2217px;width:446px;font:400 15px/30px "Roboto",sans-serif;text-align:justify}
.empower__photo{position:absolute;left:602px;top:2077px;width:484px;height:358px;border-radius:20px;background:linear-gradient(120deg,#4d4a48 0%,#7a6f66 40%,#b9a999 70%,#5d5855 100%)}

/* contact */
.contact-bg{position:absolute;left:0;top:2500px;width:1200px;height:800px;background:linear-gradient(180deg,#fff 0%,#fff 30%,#dcefe9 80%,#cfe8e1 100%)}
.contact{position:absolute;left:189px;top:2532px;width:822px;height:518px;background:var(--white);border-radius:22px;box-shadow:0 10px 40px rgba(0,0,0,.08)}
.contact__title{position:absolute;left:0;top:50px;width:822px;text-align:center;font-size:42px}
.field{position:absolute;height:50px;border-radius:25px;background:var(--white);box-shadow:0 3px 14px rgba(0,0,0,.09);font:400 14px "Roboto",sans-serif;color:#666;padding:16px 30px}
.field svg{position:absolute;right:30px;top:17px;width:15px;height:15px}

/* testimonials */
.reviews{position:absolute;left:0;top:3240px;width:1200px;height:614px;background:linear-gradient(180deg,#3a4b47 0%,#2f403c 60%,#33443f 100%)}
.reviews__title{position:absolute;left:110px;top:95px;font-size:42px;color:var(--white)}
.quote-card{position:absolute;background:var(--white);border-radius:22px;overflow:hidden}
.quote-card p{font:400 15px/29px "Roboto",sans-serif;color:#555;text-align:center}
.quote-mark{position:absolute;font:700 70px/1 Georgia,serif;color:var(--green-dark)}
.quote-card--main{left:296px;top:3430px;width:603px;height:337px;background:linear-gradient(160deg,#5d9d8c 0%,#3f7d6c 100%);border:1px solid #8cc3b5;border-radius:24px}
.quote-card--main p{color:#f0f8f5}
.signature{position:absolute;left:190px;top:240px;width:220px;height:62px;border-radius:8px;background:linear-gradient(90deg,rgba(255,255,255,.08),rgba(255,255,255,.22),rgba(255,255,255,.08))}

/* footer */
.footer h4{position:absolute;font:700 20px "Barlow Condensed",sans-serif;color:var(--ink);text-transform:uppercase}
.flist{position:absolute;list-style:none;font:400 13px/28px "Roboto",sans-serif;color:#555}
.flist li{display:flex;align-items:center;gap:12px}
.flist svg{width:12px;height:12px;flex:none}
.flist .label{color:var(--green-dark);font-weight:500}
.flist .indent{padding-left:28px}
.footer__rule{position:absolute;left:110px;top:4127px;width:905px;border-top:1px dashed var(--green-dark)}
</style>
</head>
<body>

<svg width="0" height="0" style="position:absolute">
  <defs>
    <symbol id="i-arrow" viewBox="0 0 16 16"><circle cx="8" cy="8" r="8" fill="currentColor"/><path d="M5 8h6M8.5 5l3 3-3 3" stroke="var(--bg,#2f5a4e)" stroke-width="1.8" fill="none" stroke-linecap="round" stroke-linejoin="round"/></symbol>
    <symbol id="i-diag" viewBox="0 0 12 12"><path d="M3 9l6-6M4 3h5v5" stroke="#fff" stroke-width="1.6" fill="none" stroke-linecap="round"/></symbol>
    <symbol id="i-left" viewBox="0 0 14 14"><path d="M9 3L5 7l4 4" stroke="#333" stroke-width="2" fill="none" stroke-linecap="round"/></symbol>
    <symbol id="i-right" viewBox="0 0 14 14"><path d="M5 3l4 4-4 4" stroke="#333" stroke-width="2" fill="none" stroke-linecap="round"/></symbol>
    <symbol id="i-user" viewBox="0 0 16 16"><circle cx="8" cy="5" r="3.2" fill="#666"/><path d="M2 15c0-4 3-6 6-6s6 2 6 6z" fill="#666"/></symbol>
    <symbol id="i-mail" viewBox="0 0 16 16"><rect x="1" y="3" width="14" height="10" rx="1.5" fill="#666"/><path d="M1.5 4l6.5 5 6.5-5" stroke="#fff" stroke-width="1.2" fill="none"/></symbol>
    <symbol id="i-phone" viewBox="0 0 16 16"><path d="M4 1.5l2.5 3-1.5 2c1 2 2.5 3.5 4.5 4.5l2-1.5 3 2.5-1.5 2.5C7.5 14 2 8.5 1.5 3z" fill="#666"/></symbol>
    <symbol id="i-chat" viewBox="0 0 16 16"><path d="M2 3h9v6H6l-3 2V9H2z" fill="#666"/><path d="M12 6h2v6h-1v2l-2-2H7v-2h5z" fill="#666"/></symbol>
    <symbol id="i-star" viewBox="0 0 16 16"><path d="M8 1l2.2 4.6 5 .6-3.7 3.4 1 5L8 12.2 3.5 14.6l1-5L.8 6.2l5-.6z" fill="#2f5a4e"/></symbol>
    <symbol id="i-pin" viewBox="0 0 16 16"><path d="M8 1a5 5 0 015 5c0 4-5 9-5 9S3 10 3 6a5 5 0 015-5z" fill="#2f5a4e"/><circle cx="8" cy="6" r="1.8" fill="#fff"/></symbol>
    <symbol id="i-clock" viewBox="0 0 16 16"><circle cx="8" cy="8" r="6.5" fill="none" stroke="#2f5a4e" stroke-width="1.8"/><path d="M8 4.5V8l2.5 1.5" stroke="#2f5a4e" stroke-width="1.6" fill="none"/></symbol>
    <symbol id="i-doc" viewBox="0 0 42 42"><rect x="8" y="4" width="24" height="32" rx="2" fill="none" stroke="#3f7d6c" stroke-width="2"/><path d="M13 14h14M13 20h14M13 26h9" stroke="#3f7d6c" stroke-width="2"/><circle cx="32" cy="32" r="7" fill="#fff" stroke="#3f7d6c" stroke-width="2"/></symbol>
    <symbol id="i-seal" viewBox="0 0 42 42"><circle cx="21" cy="21" r="15" fill="none" stroke="#3f7d6c" stroke-width="2"/><circle cx="21" cy="21" r="9" fill="none" stroke="#3f7d6c" stroke-width="2"/><path d="M17 21l3 3 5-6" stroke="#3f7d6c" stroke-width="2" fill="none"/></symbol>
    <symbol id="i-chart" viewBox="0 0 42 42"><path d="M6 36h30" stroke="#3f7d6c" stroke-width="2"/><rect x="9" y="22" width="6" height="12" fill="none" stroke="#3f7d6c" stroke-width="2"/><rect x="18" y="16" width="6" height="18" fill="none" stroke="#3f7d6c" stroke-width="2"/><rect x="27" y="9" width="6" height="25" fill="none" stroke="#3f7d6c" stroke-width="2"/></symbol>
  </defs>
</svg>

<!-- Hero -->
<header class="hero">
  <div class="hero__sky"></div>
  <div class="hero__city" role="img" aria-label="Harbour city skyline with sailboat"></div>
  <div class="hero__portrait" role="img" aria-label="Portrait of the accountant in a headscarf and blazer"></div>
  <div class="hero__bubble"></div>
  <svg class="abs" style="left:0;top:430px" width="1200" height="230" viewBox="0 0 1200 230">
    <path d="M0 120 C220 80 420 160 650 170 C880 180 1060 100 1200 70 L1200 230 L0 230 Z" fill="#fff"/>
    <path d="M0 120 C200 60 420 110 620 155 C820 200 1050 120 1200 75 L1200 95 C1060 150 830 215 620 195 C420 175 220 90 0 135 Z" fill="#2f5a4e"/>
  </svg>
</header>

<div class="brand" style="left:110px;top:128px;font-size:24px">Vellart <span class="brand__dot"></span></div>

<nav class="nav">
  <a style="left:0;top:0;color:var(--green-dark)">Home</a>
  <a style="left:95px;top:0">About Vellart</a>
  <a style="left:260px;top:0">Our Services</a>
  <a style="left:405px;top:0">Pricing</a>
</nav>
<div class="btn" style="left:934px;top:23px;width:154px;height:39px">Contact Us <svg style="color:#fff;--bg:#2f5a4e"><use href="#i-arrow"/></svg></div>

<div class="hero__eyebrow">LEDGRA CERTIFIED, RESULTS DRIVEN</div>
<h1 class="hero__title">WE EMPOWER<br>BUSINESSES</h1>
<p class="hero__lead">I support recipient organisations with revenue recognition, financial reporting, analysis, &amp; strategic budgeting.</p>
<div class="btn" style="left:739px;top:429px;width:146px;height:36px;background:#244a40">Get Started <svg style="color:#fff;--bg:#244a40"><use href="#i-arrow"/></svg></div>

<!-- About -->
<h2 class="heading about__title">About Vellart</h2>
<div class="about__photo" role="img" aria-label="Accountant seated on a wooden step beside a dark doorway"></div>
<div class="about__copy">
  <p>A Chartered Accountant with in-depth professional experience across New Zealand's diverse financial landscape. Throughout my career I have had the privilege of working across various sectors, including commercial organisations, charitable trusts and for purpose organisations, government-funded entities, as well as the health, disability, and education sectors.</p>
  <p>I am passionate about partnering with Small and Medium Enterprises to enhance their financial performance and drive business growth. I take pride in advising on effective strategies that support their long-term success, from streamlining financial operations to identifying new opportunities for development.</p>
</div>
<div class="btn btn--light" style="left:488px;top:1019px;width:163px;height:36px">Explore More <svg style="color:#2f5a4e;--bg:#a6d8cc"><use href="#i-arrow"/></svg></div>
<div class="badge" style="left:366px;top:1079px;width:321px"><svg><use href="#i-user" style="fill:#2f5a4e"/></svg>I am Maryam, BCom, GradDip, CA</div>
<div class="badge" style="left:710px;top:1079px;width:378px"><svg><use href="#i-star"/></svg>Ledgra Advisor Certified Professional</div>

<!-- Features -->
<section class="features">
  <div class="feature" style="left:146px"><svg><use href="#i-doc"/></svg><span>Tailored Financial Solutions</span></div>
  <div class="feature__rule" style="left:436px"></div>
  <div class="feature" style="left:522px"><svg><use href="#i-seal"/></svg><span>Ledgra Advisor Certified</span></div>
  <div class="feature__rule" style="left:762px"></div>
  <div class="feature" style="left:860px"><svg><use href="#i-chart"/></svg><span>Enhanced Financial Clarity</span></div>
</section>

<!-- Services -->
<section class="services">
  <h2 class="heading services__title">Services We Offer</h2>
  <div class="round-btn" style="left:1009px;top:57px"><svg><use href="#i-left"/></svg></div>
  <div class="round-btn" style="left:1051px;top:57px"><svg><use href="#i-right"/></svg></div>

  <article class="svc" style="left:110px;top:152px">
    <div class="svc__photo" role="img" aria-label="Woman reviewing reports at a laptop" style="background:linear-gradient(135deg,#e8e6e3,#b9b2ab 60%,#6c6662)"></div>
    <div class="svc__box"><h3>Monthly Reporting</h3><p>Regular, detailed financial reports that give you a clear view of your financial position</p></div>
    <div class="svc__go"><svg><use href="#i-diag"/></svg></div>
  </article>
  <article class="svc" style="left:379px;top:127px">
    <div class="svc__photo" role="img" aria-label="Digital cash flow graphic with floating finance icons" style="background:linear-gradient(135deg,#dfeef1,#9fc3cf 55%,#3b86b3)"></div>
    <div class="svc__box"><h3>Cash Flow Reporting</h3><p>Accurate forecasting and monitoring of your cash flow to ensure liquidity</p></div>
    <div class="svc__go"><svg><use href="#i-diag"/></svg></div>
  </article>
  <article class="svc" style="left:648px;top:152px">
    <div class="svc__photo" role="img" aria-label="Rising blue growth arrows over market data" style="background:linear-gradient(160deg,#1d3a5c,#2a5d8a 50%,#0f1f33)"></div>
    <div class="svc__box"><h3>GST, PAYE</h3><p>Compliance with GST &amp; PAYE requirements, including accurate calculations, filings, &amp; advice.</p></div>
    <div class="svc__go"><svg><use href="#i-diag"/></svg></div>
  </article>
  <article class="svc" style="left:917px;top:127px">
    <div class="svc__photo" role="img" aria-label="Hands working on a calculator beside glasses and laptop" style="background:linear-gradient(135deg,#f1f1f1,#cfcfcf 55%,#9a9a9a)"></div>
    <div class="svc__box"><h3>Payroll</h3><p>Complete payroll management, ensuring timely and compliant processing of employee</p></div>
    <div class="svc__go"><svg><use href="#i-diag"/></svg></div>
  </article>
  <div class="svc__photo" style="left:1186px;top:152px;width:40px" role="img" aria-label="Next service photo"></div>

  <svg class="abs" style="left:0;top:460px" width="1200" height="190" viewBox="0 0 1200 190">
    <path d="M0 0 C120 90 260 140 420 130 C650 110 900 50 1200 60 L1200 190 L0 190 Z" fill="#fff"/>
    <path d="M0 0 C120 90 260 150 420 140 C650 120 900 45 1200 45 L1200 60 C900 60 650 140 420 170 C260 185 100 120 0 30 Z" fill="#2f403c"/>
  </svg>
</section>

<!-- Empower -->
<h2 class="heading empower__title">Empower<br>Your Organization</h2>
<h3 class="heading empower__sub">We are proud to be Ledgra Advisor Certified</h3>
<p class="empower__copy">Providing cloud-based accounting solutions that streamline your financial processes while ensuring accuracy and compliance. Whether you're looking for help with financial reporting, budgeting, grant management, or tax filings, our dedicated team is here to support your growth and success.</p>
<div class="btn btn--light" style="left:110px;top:2384px;width:163px;height:36px">Explore More <svg style="color:#2f5a4e;--bg:#a6d8cc"><use href="#i-arrow"/></svg></div>
<div class="empower__photo" role="img" aria-label="Two colleagues smiling while working at a laptop"></div>

<!-- Contact -->
<div class="contact-bg"></div>
<section class="contact">
  <h2 class="heading contact__title">Get In Touch With Us</h2>
  <div class="field" style="left:86px;top:118px;width:312px">First Name<svg><use href="#i-user"/></svg></div>
  <div class="field" style="left:424px;top:118px;width:312px">Last Name<svg><use href="#i-user"/></svg></div>
  <div class="field" style="left:86px;top:190px;width:312px">Email Address<svg><use href="#i-mail"/></svg></div>
  <div class="field" style="left:424px;top:190px;width:312px">Phone Number<svg><use href="#i-phone"/></svg></div>
  <div class="field" style="left:86px;top:262px;width:650px;height:135px;border-radius:25px">Comments<svg><use href="#i-chat"/></svg></div>
  <div class="btn" style="left:322px;top:427px;width:180px;height:37px">Send Message <svg style="color:#fff;--bg:#2f5a4e"><use href="#i-arrow"/></svg></div>
</section>

<svg class="abs" style="left:0;top:3090px" width="1200" height="200" viewBox="0 0 1200 200">
  <path d="M0 150 C200 60 500 40 750 90 C950 130 1100 110 1200 60 L1200 200 L0 200 Z" fill="#2f403c"/>
  <path d="M170 140 C400 40 700 40 900 100 C1020 135 1120 120 1200 80 L1200 110 C1100 150 980 150 880 125 C700 80 420 70 170 140 Z" fill="#3f7d6c"/>
  <path d="M300 130 C520 70 760 80 950 120 C1060 140 1140 140 1200 125 L1200 140 C1130 160 1040 160 930 140 C760 110 520 100 300 130 Z" fill="#fff"/>
</svg>

<!-- Testimonials -->
<section class="reviews" role="region" aria-label="Customer reviews">
  <div class="abs" style="inset:0;background:linear-gradient(180deg,rgba(80,110,100,.25),rgba(40,60,55,.1))" role="img" aria-label="Faded city towers backdrop"></div>
  <h2 class="heading reviews__title">Our Happy Customers</h2>
  <div class="round-btn" style="left:1009px;top:100px"><svg><use href="#i-left"/></svg></div>
  <div class="round-btn" style="left:1051px;top:100px"><svg><use href="#i-right"/></svg></div>
</section>
<div class="quote-card" style="left:145px;top:3464px;width:200px;height:264px">
  <span class="quote-mark" style="left:38px;top:22px">&ldquo;</span>
  <p style="position:absolute;left:30px;top:58px;width:170px;text-align:left;padding-left:14px">Et harum quid tempore, cum quo minus id assumend quibusdam</p>
</div>
<div class="quote-card" style="left:850px;top:3464px;width:205px;height:264px">
  <p style="position:absolute;left:48px;top:58px;width:140px;text-align:left">. Nam libero nihil impedit nnis voluptas us autem dibus saepe</p>
  <span class="quote-mark" style="left:120px;top:200px">&rdquo;</span>
</div>
<div class="quote-card quote-card--main">
  <span class="quote-mark" style="left:44px;top:34px;color:#fff">&ldquo;</span>
  <p style="position:absolute;left:60px;top:80px;width:483px">Et harum quidem rerum facilis est et expedita distinctio. Nam libero tempore, cum soluta nobis est eligendi optio cumque nihil impedit quo minus id quod maxime placeat facere possimus, omnis voluptas assumenda est, omnis dolor repellendus. Temporibus autem quibusdam et aut officiis debitis aut rerum</p>
  <div class="signature" role="img" aria-label="Handwritten client signature"></div>
  <span class="quote-mark" style="left:520px;top:240px;color:#fff">&rdquo;</span>
</div>

<!-- Footer -->
<footer class="footer">
  <div class="brand" style="left:110px;top:4040px;font-size:30px;letter-spacing:5px;color:#2b2b2b">Vellart <span class="brand__dot" style="background:#2b2b2b"></span></div>

  <h4 style="left:355px;top:3902px">Our Location</h4>
  <ul class="flist" style="left:355px;top:3932px">
    <li><svg><use href="#i-pin"/></svg><span class="label">Email Address</span></li>
    <li class="indent">contact@vellart.co.nz</li>
    <li><svg><use href="#i-phone" style="fill:#2f5a4e"/></svg><span class="label">Phone Number</span></li>
    <li class="indent">021555018</li>
    <li><svg><use href="#i-clock"/></svg><span class="label">Working Hours</span></li>
    <li class="indent">Mon-Sat: 9am to 8pm</li>
  </ul>

  <h4 style="left:586px;top:3902px">Company</h4>
  <ul class="flist" style="left:586px;top:3932px">
    <li><svg style="color:#2f5a4e;--bg:#fff"><use href="#i-arrow"/></svg>Home</li>
    <li><svg style="color:#2f5a4e;--bg:#fff"><use href="#i-arrow"/></svg>About Us</li>
    <li><svg style="color:#2f5a4e;--bg:#fff"><use href="#i-arrow"/></svg>Our Services</li>
    <li><svg style="color:#2f5a4e;--bg:#fff"><use href="#i-arrow"/></svg>Pricing</li>
    <li><svg style="color:#2f5a4e;--bg:#fff"><use href="#i-arrow"/></svg>Testimonials</li>
    <li><svg style="color:#2f5a4e;--bg:#fff"><use href="#i-arrow"/></svg>Contact Us</li>
  </ul>

  <h4 style="left:750px;top:3902px">Resources</h4>
  <ul class="flist" style="left:750px;top:3932px">
    <li><svg style="color:#2f5a4e;--bg:#fff"><use href="#i-arrow"/></svg>Blog</li>
    <li><svg style="color:#2f5a4e;--bg:#fff"><use href="#i-arrow"/></svg>Webinars</li>
    <li><svg style="color:#2f5a4e;--bg:#fff"><use href="#i-arrow"/></svg>Announcements</li>
    <li><svg style="color:#2f5a4e;--bg:#fff"><use href="#i-arrow"/></svg>FAQs</li>
  </ul>

  <h4 style="left:923px;top:3902px">Have Questions</h4>
  <p class="abs" style="left:923px;top:3936px;width:170px;font:400 13px/24px 'Roboto',sans-serif">Get in touch with Vellart today to discuss.</p>
  <div class="btn" style="left:923px;top:4002px;width:165px;height:38px">Get A Quote <svg style="color:#fff;--bg:#2f5a4e"><use href="#i-arrow"/></svg></div>

  <div class="footer__rule"></div>
  <div class="abs" style="left:1015px;top:4117px;width:73px;height:22px;border-radius:11px;background:#2f403c;color:#fff;font:500 10px/22px 'Roboto',sans-serif;text-align:center">Go Top &#708;</div>
  <div class="abs" style="left:1133px;top:4094px;width:40px;height:40px;border-radius:50%;background:#3f7d6c;display:flex;align-items:center;justify-content:center"><svg width="18" height="18" viewBox="0 0 16 16"><path d="M2 3h12v8H7l-3 3v-3H2z" fill="#fff"/></svg></div>
  <p class="abs" style="left:110px;top:4156px;font:400 13px 'Roboto',sans-serif">(C) Copyright 2025 | All Rights Reserved</p>
  <p class="abs" style="left:950px;top:4156px;font:400 13px 'Roboto',sans-serif">Follow Us: <span style="color:#2f5a4e;font-weight:500">Netlink</span></p>
</footer>

</body>
</html>
```